Verdant Medispa Business Card

need a business card for our medispa, attached please see the logo.
our website is https://verdantmedispa-example.com

Sorina Belcourt, MD
Internal Medicine

555-204-7193

Sorina@verdantmedispa-example.com

Www.Verdantmedispa-example.com

738 E Harlow Blvd N, Ste 512, Katy, TX 77981

Target Market(s)

MedSpa, Cosmetics, Esthetics

Industry/Entity Type

MedicalSpa

Contact Information for Business Card

Please see the attached business card which i pulled from the internet. I like the idea back as a logo and front with info.

Font styles to use
Decorative

Requirements
Must have
• Color should be matching with Logo and Website theme, Also I like to have QR code for the website

```html
<!DOCTYPE html>
<html lang="en">
<head>
<meta charset="utf-8">
<title>Verdant Medispa Business Card</title>
<link rel="stylesheet" href="https://fonts.googleapis.com/css2?family=Montserrat:wght@400;500&display=swap">
<style>
  :root {
    --gold: #ae8a2d;
    --gold-text: #a8842c;
    --white: #ffffff;
    --muted: #8a7b5a;
    --canvas: #f1eee8;
    --shadow: rgba(0, 0, 0, 0.18);
  }
  * { box-sizing: border-box; margin: 0; padding: 0; }
  html, body {
    width: 1200px;
    height: 900px;
    overflow: hidden;
    background: var(--canvas);
    font-family: "Montserrat", Arial, sans-serif;
  }
  .canvas {
    position: relative;
    width: 1200px;
    height: 900px;
  }
  .card {
    position: absolute;
    width: 580px;
    height: 340px;
    box-shadow: 0 14px 30px var(--shadow);
    overflow: hidden;
  }
  .card--front {
    left: 310px;
    top: 70px;
    background: var(--white);
  }
  .card--back {
    left: 310px;
    top: 480px;
    background: var(--gold);
  }
  .brand {
    display: flex;
    align-items: center;
    justify-content: center;
    gap: 12px;
    font-weight: 400;
    letter-spacing: 0.08em;
  }
  .brand__dot {
    width: 12px;
    height: 12px;
    border-radius: 50%;
    background: currentColor;
  }
  .card--front .brand {
    position: absolute;
    top: 60px;
    left: 0;
    right: 0;
    color: var(--gold-text);
    font-size: 26px;
  }
  .card--back .brand {
    position: absolute;
    top: 0;
    bottom: 0;
    left: 0;
    right: 0;
    color: var(--white);
    font-size: 40px;
  }
  .identity {
    position: absolute;
    top: 176px;
    right: 325px;
    text-align: right;
  }
  .identity__name {
    color: var(--gold-text);
    font-size: 20px;
    font-weight: 500;
    white-space: nowrap;
  }
  .identity__title {
    margin-top: 12px;
    color: var(--muted);
    font-size: 12px;
  }
  .divider {
    position: absolute;
    left: 276px;
    top: 172px;
    width: 1px;
    height: 70px;
    background: var(--gold-text);
  }
  .contacts {
    position: absolute;
    left: 294px;
    top: 172px;
    list-style: none;
  }
  .contacts__item {
    display: flex;
    align-items: center;
    gap: 10px;
    height: 24px;
    color: var(--gold-text);
    font-size: 12px;
    white-space: nowrap;
  }
  .contacts__icon {
    width: 13px;
    height: 13px;
    fill: var(--muted);
    flex: none;
  }
  .address-band {
    position: absolute;
    left: 0;
    right: 0;
    bottom: 0;
    height: 42px;
    background: var(--gold);
    color: var(--white);
    font-size: 12px;
    display: flex;
    align-items: center;
    justify-content: center;
  }
  .qr-slot {
    position: absolute;
    right: 24px;
    bottom: 24px;
    width: 64px;
    height: 64px;
    background: var(--white);
    border-radius: 4px;
  }
</style>
</head>
<body>
<main class="canvas">
  <section class="card card--front" aria-label="Business card front">
    <div class="brand"><span class="brand__dot"></span>Verdant Medispa</div>

    <div class="identity">
      <p class="identity__name">Sorina Belcourt, MD</p>
      <p class="identity__title">Internal Medicine</p>
    </div>

    <div class="divider"></div>

    <ul class="contacts">
      <li class="contacts__item">
        <svg class="contacts__icon" viewBox="0 0 24 24" aria-hidden="true"><path d="M6.6 10.8a15 15 0 0 0 6.6 6.6l2.2-2.2a1 1 0 0 1 1-.25 11.4 11.4 0 0 0 3.6.57 1 1 0 0 1 1 1V20a1 1 0 0 1-1 1A17 17 0 0 1 3 4a1 1 0 0 1 1-1h3.5a1 1 0 0 1 1 1c0 1.25.2 2.45.57 3.57a1 1 0 0 1-.25 1z"/></svg>
        555-204-7193
      </li>
      <li class="contacts__item">
        <svg class="contacts__icon" viewBox="0 0 24 24" aria-hidden="true"><path d="M2 5h20v14H2z M3.5 6.5 12 12.5l8.5-6V6.5H3.5z" fill-rule="evenodd"/></svg>
        Sorina@verdantmedispa-example.com
      </li>
      <li class="contacts__item">
        <svg class="contacts__icon" viewBox="0 0 24 24" aria-hidden="true"><path d="M12 2a10 10 0 1 0 0 20 10 10 0 0 0 0-20zm6.9 6h-3a15 15 0 0 0-1.3-3.9A8 8 0 0 1 18.9 8zM12 4a13 13 0 0 1 1.9 4h-3.8A13 13 0 0 1 12 4zM4.3 14a8 8 0 0 1 0-4h3.4a16 16 0 0 0 0 4zm.8 2h3a15 15 0 0 0 1.3 3.9A8 8 0 0 1 5.1 16zm3-8h-3a8 8 0 0 1 4.3-3.9A15 15 0 0 0 8.1 8zM12 20a13 13 0 0 1-1.9-4h3.8A13 13 0 0 1 12 20zm2.3-6H9.7a14 14 0 0 1 0-4h4.6a14 14 0 0 1 0 4zm.3 5.9a15 15 0 0 0 1.3-3.9h3a8 8 0 0 1-4.3 3.9zm1.7-5.9a16 16 0 0 0 0-4h3.4a8 8 0 0 1 0 4z"/></svg>
        Www.Verdantmedispa-example.com
      </li>
    </ul>

    <div class="address-band">738 E Harlow Blvd N, Ste 512, Katy, TX 77981</div>
  </section>

  <section class="card card--back" aria-label="Business card back">
    <div class="brand"><span class="brand__dot"></span>Verdant Medispa</div>
    <div class="qr-slot" role="img" aria-label="Space for a QR code linking to the website"></div>
  </section>
</main>
</body>
</html>
```